Counselling business requires poster

I require a poster to promote my counselling and coaching business I will be placing these in doctors surgery's and clinics etc.
This business is centred around helping people work through emotional issues. We provided one on one sessions which help enhance peoples lives by assisting them in overcoming their fears, obsessions, insecurities etc.

We offer support in a broad range of areas:

- Eating disorders & weight managment
- Depression
- Marriage and relationship issues
- Anxiety
- Victims of physical, verbal and/or social abuse

We want our poster to be representative of the positive, warm and welcoming atmosphere we provide.

Our motto, 'One step at a time', is symbolic of our approach and how we help our clients to tackle their problems bit by bit.

The flyer I have uploaded is just some information on what we offer

Thankyou for your designs I am taking them into consideration and will inform you of any decision.

Weight

```html
<!DOCTYPE html>
<html lang="en">
<head>
<meta charset="utf-8">
<title>Harbourview Counselling – One Step at a Time</title>
<link rel="stylesheet" href="https://fonts.googleapis.com/css2?family=Lato:wght@300;400;700&family=Teko:wght@400;500&display=swap">
<style>
  :root{
    --slate:#566a8c;
    --slate-dark:#4a5c7c;
    --slate-mid:#6f82a3;
    --slate-light:#8e9fbd;
    --sky:#a8d3f7;
    --ink:#1d2330;
    --title:#4b5a75;
    --white:#ffffff;
  }
  *{box-sizing:border-box;margin:0;padding:0}
  html,body{width:878px;height:1200px;overflow:hidden;background:#ffffff}
  .poster{position:relative;width:878px;height:1200px;overflow:hidden;background:var(--white);font-family:'Lato',sans-serif}
  .backdrop{position:absolute;inset:0}
  .brand{position:absolute;top:34px;right:40px;text-align:right;font-weight:300;color:var(--title);font-size:54px;line-height:60px;letter-spacing:1px;white-space:nowrap}
  .motto{position:absolute;right:40px;top:244px;text-align:right;font-family:'Teko',sans-serif;font-weight:500;color:var(--sky);line-height:.85;white-space:nowrap}
  .motto__lead{display:block;font-size:100px;letter-spacing:1px}
  .motto__tail{display:block;font-size:62px;letter-spacing:1px;margin-top:6px}
  .intro{position:absolute;right:40px;top:438px;width:190px;text-align:right;color:var(--white);font-size:16.5px;line-height:24px}
  .goal{position:absolute;right:40px;top:626px;width:320px;text-align:right;color:var(--white);font-size:16.5px;line-height:22px}
  .approach{position:absolute;right:40px;top:796px;width:440px;text-align:right;color:var(--ink);font-size:15px;line-height:21px}
  .stat{position:absolute;left:290px;right:0;top:870px;height:44px;background:linear-gradient(90deg,rgba(142,159,189,0) 0%,var(--slate-light) 12%,var(--slate-light) 100%);color:var(--white);font-family:'Teko',sans-serif;font-weight:500;font-size:19px;line-height:47px;text-align:right;padding-right:36px;white-space:nowrap}
  .invite{position:absolute;right:40px;top:930px;width:560px;text-align:right;color:var(--ink);font-size:15.5px;line-height:22px}
  .services{position:absolute;left:0;right:0;top:1012px;height:188px}
  .service{position:absolute;top:0;height:188px;color:var(--white)}
  .service__head{position:absolute;top:18px;display:flex;align-items:center;gap:9px;font-family:'Teko',sans-serif;font-weight:500;font-size:27px;line-height:1;white-space:nowrap}
  .service__head svg{flex:none}
  .service__body{position:absolute;top:70px;font-size:14px;line-height:18px}
  .service--abuse .service__head{left:34px}
  .service--abuse .service__body{left:34px;width:260px}
  .service--family .service__head{left:336px}
  .service--family .service__body{left:336px;width:232px}
  .service--depression .service__head{left:620px}
  .service--depression .service__body{left:620px;width:226px}
  .badge{position:absolute;left:100px;top:398px;width:220px;height:220px;border-radius:50%;background:var(--slate);display:flex;align-items:center;justify-content:center}
  .badge__inner{width:192px;height:192px;border-radius:50%;background:var(--sky);display:flex;align-items:center;justify-content:center;text-align:center;color:var(--slate-dark);font-weight:700;font-size:19px;line-height:26px}
</style>
</head>
<body>
<main class="poster">
  <svg class="backdrop" width="878" height="1200" viewBox="0 0 878 1200">
    <defs>
      <linearGradient id="tone-distress" x1="0" y1="0" x2="1" y2="1">
        <stop offset="0" stop-color="#d9d2cb"/><stop offset="1" stop-color="#8a7e76"/>
      </linearGradient>
      <linearGradient id="tone-stress" x1="0" y1="0" x2="1" y2="1">
        <stop offset="0" stop-color="#e6e4e2"/><stop offset="1" stop-color="#7d8b96"/>
      </linearGradient>
      <linearGradient id="tone-weight" x1="1" y1="0" x2="0" y2="1">
        <stop offset="0" stop-color="#6fb2e8"/><stop offset="0.55" stop-color="#e9d8cc"/><stop offset="1" stop-color="#d9a98d"/>
      </linearGradient>
    </defs>

    <polygon points="0,0 150,0 0,150" fill="var(--slate)"/>
    <polygon points="0,770 242,1012 0,1012" fill="var(--slate)"/>
    <rect x="400" y="215" width="478" height="560" fill="var(--slate)"/>

    <polygon points="210,-16 456,230 210,476 -36,230" fill="var(--slate)"/>
    <polygon points="210,-6 446,230 210,466 -26,230" fill="var(--white)"/>
    <polygon points="210,2 438,230 210,458 -18,230" fill="url(#tone-distress)" role="img" aria-label="Photo of a distressed man holding his head in his hands"/>

    <polygon points="440,270 630,460 440,650 250,460" fill="var(--slate-dark)"/>
    <polygon points="440,278 622,460 440,642 258,460" fill="var(--white)"/>
    <polygon points="440,286 614,460 440,634 266,460" fill="url(#tone-stress)" role="img" aria-label="Photo of a stressed young woman pressing her temples"/>

    <polygon points="220,524 456,760 220,996 -16,760" fill="var(--slate)"/>
    <polygon points="220,532 448,760 220,988 -8,760" fill="var(--white)"/>
    <polygon points="220,540 440,760 220,980 0,760" fill="url(#tone-weight)" role="img" aria-label="Photo of a tape measure wrapped around a waist against blue sky"/>

    <polygon points="0,1012 300,1012 360,1106 300,1200 0,1200" fill="var(--slate)"/>
    <polygon points="300,1012 582,1012 642,1106 582,1200 300,1200 360,1106" fill="var(--slate-mid)"/>
    <polygon points="582,1012 878,1012 878,1200 582,1200 642,1106" fill="var(--slate-light)"/>
  </svg>

  <h1 class="brand">HARBOURVIEW<br>COUNSELLING</h1>

  <h2 class="motto"><span class="motto__lead">ONE STEP</span><span class="motto__tail">AT A TIME</span></h2>

  <div class="badge"><div class="badge__inner">PROFESSIONAL<br>AND<br>CONFIDENTIAL<br>SERVICE</div></div>

  <p class="intro">Today you are one<br>step closer to a<br>new you where you<br>feel empowered<br>and on a positive<br>path to<br>well&#8209;being.</p>
  <p class="goal">My goal is to help you uncover your true potential and lead a life that is worth celebrating.</p>

  <p class="approach">We will unearth long-standing behaviour patterns or negative perceptions that may be holding you back from experiencing a more fulfilling and meaningful life.</p>

  <div class="stat">TRADITIONAL WEIGHT LOSS PROGRAMS HAVE UP TO AN 80% FAILURE RATE</div>

  <p class="invite">If you're looking for extra support and guidance through a challenging situation or you're just ready to move in a new direction in your life, I look forward to working with you to achieve your goals</p>

  <section class="services">
    <article class="service service--abuse">
      <h3 class="service__head">
        <svg width="40" height="40" viewBox="0 0 46 46"><circle cx="23" cy="23" r="23" fill="var(--white)"/><rect x="14" y="20" width="18" height="16" rx="5" fill="var(--slate)"/><rect x="14" y="11" width="4" height="12" rx="2" fill="var(--slate)"/><rect x="19.5" y="9" width="4" height="13" rx="2" fill="var(--slate)"/><rect x="25" y="10" width="4" height="12" rx="2" fill="var(--slate)"/><rect x="30" y="14" width="4" height="10" rx="2" fill="var(--slate)"/></svg>
        ABUSE
      </h3>
      <p class="service__body">One of the main characteristics of an abusive relationship is control, when one person is doing something to control the behaviour of the other and it becomes entrenched.</p>
    </article>
    <article class="service service--family">
      <h3 class="service__head">
        <svg width="40" height="40" viewBox="0 0 46 46"><circle cx="23" cy="23" r="23" fill="var(--white)"/><circle cx="14" cy="17" r="4" fill="var(--slate-mid)"/><circle cx="32" cy="17" r="4" fill="var(--slate-mid)"/><circle cx="23" cy="24" r="4" fill="var(--slate-mid)"/><path d="M7 30a7 7 0 0 1 14 0zM25 30a7 7 0 0 1 14 0zM15 38a8 8 0 0 1 16 0z" fill="var(--slate-mid)"/></svg>
        FAMILY COUNSELLING
      </h3>
      <p class="service__body">Most, if not all intimate relationships will experience difficulty at some point and if you and your partner are experiencing problems in your relationship.</p>
    </article>
    <article class="service service--depression">
      <h3 class="service__head">
        <svg width="40" height="40" viewBox="0 0 46 46"><circle cx="23" cy="23" r="23" fill="var(--white)"/><circle cx="23" cy="23" r="15" fill="none" stroke="var(--slate-light)" stroke-width="2.5"/><circle cx="18" cy="19" r="2" fill="var(--slate-light)"/><circle cx="28" cy="19" r="2" fill="var(--slate-light)"/><path d="M16 31q7-7 14 0" fill="none" stroke="var(--slate-light)" stroke-width="2.5" stroke-linecap="round"/></svg>
        DEPRESSION
      </h3>
      <p class="service__body">Depression and anxiety are nothing to be ashamed of. We sometimes have bouts of anxiety or depression that we recover from fairly quickly.</p>
    </article>
  </section>
</main>
</body>
</html>
```